Classic and neutral book cover design

We are looking for a classic and neutral book cover design to be used as the template for a series of books to be published. We are hence looking for a template that will allow us to easily change the title name for all books in this series.
The use of very few colours (black and white is welcome) and few design elements is a big bonus. As a source of inspiration we would like to ask you to view the very simple and
If you think you have a cool idea that can add a twist to the formal classic look don't hesitate. Go for it !
Work will be done for a 30 year old Sweden based cultural non-profit called VĂ©lra (www.velrafoundation.example). We work with the publishing and supporting of post-modern art and literature addressing contemporary topics but are also involved in assisting projects of cultural preservation.
Target Market(s)
The audience is expected to have some form of interest in culture but could range from hobbyist readers to tenure track scholars
Industry/Entity Type
Non-Profit
Requirements
Must have
- General:
- Classic and neutral feel
- Preferably very simple and few shapes
- usage of few colours (black and white is welcome)
Information to be displayed on the cover is:
- Author
- Title
- type of work e.g. play/novel (optional)
- publishing house (in this case "Velra Publishing")
Nice to have
- ideas to prevent it from become boring are of course welcome
Should not have
- - too many colours

```html
<!DOCTYPE html>
<html lang="en">
<head>
<meta charset="UTF-8">
<title>Velra Publishing – Book Cover</title>
<link rel="stylesheet" href="https://fonts.googleapis.com/css2?family=Antonio:wght@300;400&family=Oswald:wght@600&display=swap">
<style>
  :root {
    --page: #ffffff;
    --paper: #e6ddd4;
    --frame: #a89ca2;
    --hairline: #c9c0b9;
    --ink: #111111;
  }
  * { margin: 0; padding: 0; box-sizing: border-box; }
  html, body {
    width: 1200px;
    height: 900px;
    overflow: hidden;
    background: var(--page);
  }
  .cover {
    position: absolute;
    left: 300px;
    top: 0;
    width: 608px;
    height: 900px;
    background: var(--paper);
    color: var(--ink);
  }
  .cover__hairline {
    position: absolute;
    left: 36px;
    top: 32px;
    width: 536px;
    height: 836px;
    border: 1px solid var(--hairline);
  }
  .cover__frames {
    position: absolute;
    left: 0;
    top: 0;
  }
  .cover__text {
    position: absolute;
    left: 0;
    width: 100%;
    text-align: center;
    transform: translateY(-50%);
    line-height: 1;
  }
  .cover__author {
    top: 166px;
    font-family: "Antonio", sans-serif;
    font-weight: 400;
    font-size: 34px;
  }
  .cover__title {
    top: 347px;
    font-family: "Antonio", sans-serif;
    font-weight: 400;
    font-size: 80px;
    letter-spacing: -1px;
  }
  .cover__genre {
    top: 474px;
    font-family: "Antonio", sans-serif;
    font-weight: 300;
    font-size: 32px;
  }
  .cover__publisher {
    top: 785px;
    font-family: "Oswald", sans-serif;
    font-weight: 600;
    font-size: 23px;
    letter-spacing: 2px;
  }
  .cover__publisher-rule {
    position: absolute;
    left: 198px;
    top: 803px;
    width: 206px;
    height: 2px;
    background: var(--frame);
  }
</style>
</head>
<body>
  <main class="cover">
    <div class="cover__hairline"></div>
    <svg class="cover__frames" width="608" height="900" viewBox="0 0 608 900" aria-hidden="true">
      <rect x="64" y="62" width="482" height="777" rx="12" ry="12" fill="none" stroke="var(--frame)" stroke-width="3"/>
      <rect x="76" y="75" width="457" height="752" rx="9" ry="9" fill="none" stroke="var(--frame)" stroke-width="3"/>
    </svg>
    <p class="cover__text cover__author">AUTHOR</p>
    <h1 class="cover__text cover__title">Title</h1>
    <p class="cover__text cover__genre">Novel</p>
    <p class="cover__text cover__publisher">VELRA PUBLISHING</p>
    <div class="cover__publisher-rule"></div>
  </main>
</body>
</html>
```